Rack Cards

We need a series of (4) Rack Card size "postcards" to have the same design but different wording. The rack cards need to include our logo and be in our branding colors (espresso brown and orangey copper.) The card needs to be double sided, with verbage on one side and our logo and jewelry pictures on the other side. Please use josefin font to match our logo. Also, please keep diamond pictures with bridal, colored stone jewelry to be dispersed between remaining cards. More jewelry pictures available upon request.
See attached files for logo, wording and jewelry pictures.
Updates
Sorry for the error in sizing. The correct size of the rack cards should be 8.27" long by 3.74" wide.
Industry/Entity Type
Jewelry
Look and feel

```html
<!DOCTYPE html>
<html lang="en">
<head>
<meta charset="utf-8">
<title>Holloway's – Colored Gemstones Rack Card</title>
<link rel="stylesheet" href="https://fonts.googleapis.com/css2?family=Josefin+Sans:wght@300&family=Gelasio:wght@400&display=swap">
<style>
  :root {
    --copper: #c94a22;
    --espresso-rust: #8a2c1b;
    --panel-grey: #d5d4d2;
    --ink-white: #ffffff;
    --canvas-white: #ffffff;
    --photo-light: #f6f6f8;
    --photo-silver: #dcdde3;
    --photo-violet: #8f86d6;
  }
  * { box-sizing: border-box; margin: 0; padding: 0; }
  html, body {
    width: 1114px;
    height: 1200px;
    overflow: hidden;
    background: var(--canvas-white);
  }
  .rack-card {
    position: relative;
    width: 1114px;
    height: 1200px;
    background: var(--canvas-white);
  }
  .brand-band {
    position: absolute;
    left: 15px;
    top: 12px;
    width: 535px;
    height: 237px;
    background: var(--copper);
    color: var(--ink-white);
    font-family: "Gelasio", Georgia, serif;
    font-weight: 400;
    display: flex;
    flex-direction: column;
    align-items: center;
    justify-content: center;
    gap: 14px;
  }
  .brand-name {
    display: flex;
    align-items: center;
    gap: 18px;
    font-size: 64px;
    line-height: 1;
  }
  .brand-dot {
    width: 18px;
    height: 18px;
    border-radius: 50%;
    background: var(--ink-white);
  }
  .brand-tagline {
    font-size: 24px;
    letter-spacing: 2px;
  }
  .brand-rule {
    position: absolute;
    left: 15px;
    top: 252px;
    width: 535px;
    height: 4px;
    background: var(--espresso-rust);
  }
  .jewelry-photo {
    position: absolute;
    left: 15px;
    top: 275px;
    width: 535px;
    height: 600px;
    background: radial-gradient(ellipse at 45% 45%, var(--photo-violet) 0%, var(--photo-silver) 28%, var(--photo-light) 60%, var(--canvas-white) 100%);
  }
  .copy-panel {
    position: absolute;
    left: 567px;
    top: 12px;
    width: 535px;
    height: 1188px;
    background: var(--panel-grey);
    color: var(--ink-white);
    text-align: center;
  }
  .copy-title {
    font-family: "Josefin Sans", sans-serif;
    font-weight: 300;
    font-size: 44px;
    line-height: 50px;
    letter-spacing: 0.5px;
    margin-top: 96px;
  }
  .copy-text {
    font-family: "Gelasio", Georgia, serif;
    font-size: 18.5px;
    line-height: 24px;
    width: 400px;
    margin: 0 auto;
  }
  .copy-text.intro { margin-top: 44px; }
  .copy-text.selection { margin-top: 42px; }
  .copy-text.care { margin-top: 54px; }
</style>
</head>
<body>
<main class="rack-card">
  <header class="brand-band">
    <div class="brand-name"><span class="brand-dot"></span>Holloway's</div>
    <div class="brand-tagline">Fine Jewelry Studio</div>
  </header>
  <div class="brand-rule"></div>

  <div class="jewelry-photo" role="img" aria-label="Platinum ring with a cushion-cut violet sapphire flanked by two emerald-cut diamonds"></div>

  <section class="copy-panel">
    <h1 class="copy-title">Colored Gemstones</h1>
    <p class="copy-text intro">At Holloway's, we have a passion for colored gemstones.&nbsp; We have one of the largest natural loose gemstone collections in all of New England.&nbsp; The gems that we carry are, without compromise, some of the very finest and most rare available in the world today.&nbsp; From the far reaches of the globe, Holloway's acquires only natural gemstones of exceptional quality.</p>
    <p class="copy-text selection">All of the colored gemstones at Holloway's are individually selected to ensure that our collection properly displays just how unique and rare gemstones can be.&nbsp; We pride ourselves on carrying the uncommon colored gemstones; the beautiful gifts from Mother Nature that you won't find everywhere.&nbsp; We believe that because gemstones are so rare and unique, they should also be of the highest quality.&nbsp; The correct combination of hue, saturation and tone.&nbsp; A cut that brings out a gemstone's brilliance or makes it into something you've never seen before.&nbsp; We work closely with world-renowned gemstone suppliers, as well as master gem cutting artists to find gemstones that we are proud to present and that you will want to wear.</p>
    <p class="copy-text care">Holloway's offers free lifetime cleaning and inspection of your colored gemstone jewelry purchase. Just stop by the store and we'll make sure your jewelry looks as good as the day it was purchased.&nbsp; You should do this a minimum of every six months.</p>
  </section>
</main>
</body>
</html>
```